Plumwick Home - High Quality Organic Cleaning Product

A product label for a foaming hand soap. Company is called "Plumwick Home" and the tagline is "The Plumwick Promise". Maybe lighter blue background with red letters, but open to what looks good. Want it to be a simple, clean and sophisticated design that looks fresh and stands out. This product has high quality organic ingredients hence the ingredients are "plumwick home" than other toxic chemical cleaners. Attached is label specifications as well as an image for stock language for left and right side of label for reference. Parts can be omitted, added or mixed and matched as needed.
Went on vacation/holiday
Moms

```html
<!DOCTYPE html>
<html lang="en">
<head>
<meta charset="utf-8">
<title>Plumwick Home – Foaming Hand Soap Label</title>
<link rel="stylesheet" href="https://fonts.googleapis.com/css2?family=Fraunces:opsz,wght@9..144,500;9..144,700&family=Kaushan+Script&family=Montserrat:wght@900&family=Roboto:wght@400;500&display=swap">
<style>
  :root {
    --page: #f4f5f7;
    --blue-deep: #1b7bbd;
    --blue-mid: #3a93c9;
    --blue-light: #6cb0d7;
    --white: #ffffff;
    --lime: #86ec3c;
    --volume-blue: #2f80b9;
  }
  * { box-sizing: border-box; margin: 0; padding: 0; }
  html, body {
    width: 1089px;
    height: 1200px;
    overflow: hidden;
    background: var(--page);
  }
  .label {
    position: absolute;
    left: 196px;
    top: 40px;
    width: 696px;
    height: 1120px;
    background: linear-gradient(90deg, var(--blue-mid) 0%, var(--blue-light) 22%, var(--blue-mid) 55%, var(--blue-deep) 100%);
    overflow: hidden;
    color: var(--white);
    text-align: center;
  }
  .brand-name {
    position: absolute;
    left: 0; right: 0;
    top: 78px;
    font-family: "Fraunces", Georgia, serif;
    font-weight: 700;
    font-size: 54px;
    line-height: 1;
  }
  .brand-tagline {
    position: absolute;
    left: 0; right: 0;
    top: 152px;
    font-family: "Roboto", Arial, sans-serif;
    font-weight: 400;
    font-size: 28px;
    line-height: 1;
    letter-spacing: 1px;
  }
  .product-style {
    position: absolute;
    left: 0; right: 0;
    top: 290px;
    font-family: "Kaushan Script", cursive;
    font-size: 104px;
    line-height: 1;
    color: var(--lime);
  }
  .product-name {
    position: absolute;
    left: 0; right: 0;
    top: 418px;
    font-family: "Montserrat", Arial, sans-serif;
    font-weight: 900;
    font-size: 160px;
    line-height: 138px;
    letter-spacing: 2px;
  }
  .product-note {
    position: absolute;
    left: 0; right: 0;
    top: 720px;
    font-family: "Fraunces", Georgia, serif;
    font-weight: 500;
    font-size: 32px;
    line-height: 1;
    color: var(--lime);
  }
  .bubble-band {
    position: absolute;
    left: 0; right: 0;
    top: 772px;
    height: 230px;
    background: linear-gradient(180deg, rgba(255,255,255,0) 0%, rgba(255,255,255,0.55) 35%, var(--white) 75%);
  }
  .label-foot {
    position: absolute;
    left: 0; right: 0;
    top: 1000px;
    bottom: 0;
    background: var(--white);
  }
  .volume {
    position: absolute;
    left: 0; right: 0;
    top: 1028px;
    font-family: "Roboto", Arial, sans-serif;
    font-weight: 500;
    font-size: 31px;
    line-height: 1;
    color: var(--volume-blue);
  }
</style>
</head>
<body>
  <section class="label" aria-label="Plumwick Home foaming hand soap label">
    <p class="brand-name">Plumwick Home</p>
    <p class="brand-tagline">The Plumwick Promise</p>

    <p class="product-style">Foaming</p>
    <h1 class="product-name">HAND<br>SOAP</h1>
    <p class="product-note">with organic ingredients</p>

    <div class="bubble-band" role="img" aria-label="Decorative band of soap bubbles and sparkles"></div>
    <div class="label-foot"></div>
    <p class="volume">8 FL. OZ (236ML)</p>
  </section>
</body>
</html>
```